Vintage label design for Electrical company (stickers)

I'm after a vintage label design for my electrical company, currently trying to break into the upper market in the electrical field so I need something that stands out and is easy to read.
These will be getting made into stickers roughly 90-110mm x 40-60mm with a custom rectangular shape.
The stickers should have

Target Market(s)

Upper electrical market

Industry/Entity Type

Electrical

Font styles to use
Serif
Decorative
Script

Colors
acd037
9ccb3b
33b8a4

Requirements
Must have
• Be unique, edgy, vintage/retro and easy to read. An electrical theme
• Company logo (picture provided below obviously a lime)
• Fern Voltworks
• 0428915043
• Fernvoltworks.com
• Socialbook symbol
• as these are going to be stickers I would like my contact details on them
Nice to have
• Same shades of green, fit between 90-110mm x 40-60mm

```html
<!DOCTYPE html>
<html lang="en">
<head>
<meta charset="utf-8">
<title>Fern Voltworks Label</title>
<link rel="stylesheet" href="https://fonts.googleapis.com/css2?family=Lobster&family=Montserrat:wght@500&family=Yellowtail&display=swap">
<style>
  :root {
    --page-bg: #e4e9dc;
    --label-bg: #ecefdf;
    --forest: #0b4a06;
    --leaf: #93c56d;
    --bolt: #a3864f;
  }
  html, body {
    margin: 0;
    padding: 0;
    width: 1200px;
    height: 1200px;
    overflow: hidden;
    background: var(--page-bg);
  }
  .canvas {
    position: relative;
    width: 1200px;
    height: 1200px;
  }
  .label {
    position: absolute;
    left: 282px;
    top: 167px;
    width: 628px;
    height: 831px;
    box-sizing: border-box;
    border: 1.5px solid var(--forest);
    background: var(--label-bg);
  }
  .frame-band {
    position: absolute;
    left: 302px;
    top: 186px;
    width: 588px;
    height: 588px;
    box-sizing: border-box;
    border: 11px solid var(--leaf);
  }
  .frame-inner {
    position: absolute;
    left: 329px;
    top: 214px;
    width: 533px;
    height: 533px;
    box-sizing: border-box;
    border: 1.5px solid var(--forest);
  }
  .emblem {
    position: absolute;
    left: 512px;
    top: 222px;
    width: 186px;
    height: 230px;
  }
  .established {
    position: absolute;
    left: 616px;
    top: 458px;
    font-family: "Montserrat", sans-serif;
    font-weight: 500;
    font-size: 18px;
    letter-spacing: 1.5px;
    color: var(--leaf);
  }
  .brand-main {
    position: absolute;
    left: 360px;
    top: 440px;
    width: 480px;
    text-align: center;
    font-family: "Lobster", cursive;
    font-size: 150px;
    line-height: 1;
    color: var(--forest);
    transform: rotate(-4deg);
  }
  .brand-sub {
    position: absolute;
    left: 430px;
    top: 600px;
    width: 380px;
    text-align: center;
    font-family: "Yellowtail", cursive;
    font-size: 86px;
    line-height: 1;
    color: var(--leaf);
    transform: rotate(-9deg);
  }
  .swoosh {
    position: absolute;
    left: 496px;
    top: 676px;
    width: 284px;
    height: 56px;
  }
  .phone-row {
    position: absolute;
    left: 364px;
    top: 790px;
    width: 464px;
    height: 90px;
    display: flex;
    align-items: center;
    justify-content: space-between;
  }
  .phone-icon { width: 70px; height: 52px; }
  .phone-number {
    font-family: "Lobster", cursive;
    font-size: 80px;
    line-height: 1;
    color: var(--forest);
  }
  .rule {
    position: absolute;
    left: 364px;
    width: 464px;
    height: 1.5px;
    background: var(--forest);
  }
  .contact-row {
    position: absolute;
    left: 364px;
    top: 904px;
    width: 464px;
    height: 36px;
    display: flex;
    align-items: center;
    font-family: "Lobster", cursive;
    font-size: 23px;
    color: var(--forest);
  }
  .contact-web {
    width: 232px;
    display: flex;
    align-items: center;
    gap: 8px;
  }
  .contact-web svg { width: 20px; height: 20px; }
  .contact-divider {
    width: 1.5px;
    height: 40px;
    background: var(--forest);
  }
  .contact-social {
    flex: 1;
    display: flex;
    align-items: center;
    justify-content: flex-end;
    gap: 10px;
  }
  .social-square {
    width: 19px;
    height: 19px;
    background: var(--forest);
    border-radius: 2px;
  }
  .bottom-band {
    position: absolute;
    left: 302px;
    top: 968px;
    width: 588px;
    height: 18px;
    background: var(--leaf);
  }
</style>
</head>
<body>
<div class="canvas">
  <div class="label"></div>
  <div class="frame-band"></div>
  <div class="frame-inner"></div>

  <svg class="emblem" viewBox="0 0 186 230" role="img" aria-label="Illustration of a halved lime with a lightning bolt striking its centre">
    <circle cx="94" cy="138" r="88" fill="var(--leaf)"/>
  </svg>

  <div class="established">EST. 2015</div>
  <div class="brand-main">Fern</div>
  <div class="brand-sub">Voltworks</div>
  <svg class="swoosh" viewBox="0 0 284 56">
    <path d="M8 48 C90 34 190 20 276 8" fill="none" stroke="var(--leaf)" stroke-width="7" stroke-linecap="round"/>
  </svg>

  <div class="phone-row">
    <svg class="phone-icon" viewBox="0 0 70 52" aria-hidden="true">
      <path d="M4 20 C4 6 66 6 66 20 L66 24 L50 24 L50 16 L20 16 L20 24 L4 24 Z" fill="var(--forest)"/>
      <path d="M18 22 L52 22 L64 44 L64 50 L6 50 L6 44 Z" fill="var(--forest)"/>
      <circle cx="35" cy="36" r="8" fill="var(--label-bg)"/>
      <circle cx="35" cy="36" r="3.5" fill="var(--forest)"/>
    </svg>
    <span class="phone-number">0428915043</span>
  </div>

  <div class="rule" style="top:894px"></div>
  <div class="rule" style="top:898px"></div>

  <div class="contact-row">
    <div class="contact-web">
      <svg viewBox="0 0 20 20" aria-hidden="true" fill="none" stroke="var(--forest)" stroke-width="1.2">
        <circle cx="10" cy="10" r="8.5"/>
        <ellipse cx="10" cy="10" rx="4" ry="8.5"/>
        <line x1="1.5" y1="10" x2="18.5" y2="10"/>
        <line x1="3" y1="5.5" x2="17" y2="5.5"/>
        <line x1="3" y1="14.5" x2="17" y2="14.5"/>
      </svg>
      <span>Fernvoltworks.com</span>
    </div>
    <div class="contact-divider"></div>
    <div class="contact-social">
      <span>/Socialbook link</span>
      <span class="social-square"></span>
    </div>
  </div>

  <div class="rule" style="top:944px"></div>
  <div class="rule" style="top:948px"></div>

  <div class="bottom-band"></div>
</div>
</body>
</html>
```